Business Card

Hello! We need a business card for a kid's ski shop in Vail, CO. During the Fall/Winter months, we are primarily a children's ski outfitter; however, we also carry many high end boutique items. Our age ranges are from Birth to about age 15. Our clientele come from all over the world. We would like a business card that is timeless, but fun considering we are a children's store. We have a large web presence and are really trying to brand our website www.TotTrailhub.com. Since we have such a tourist clientele, we try to remind them that they can shop 365 at our website. I have attached our new logos. Here is our store info:
PipTrek
418 W. Birch Ln., Suite F7
Larkmoor, MT 59031
970-528-3094
www.TotTrailhub.com

```html
<!DOCTYPE html>
<html lang="en">
<head>
<meta charset="utf-8">
<title>PipTrek Business Card</title>
<link rel="stylesheet" href="https://fonts.googleapis.com/css2?family=Open+Sans:wght@400;600;700&display=swap">
<style>
  :root {
    --stage: #e7e4e0;
    --brand-red: #ed1c24;
    --ink-black: #0d0d0d;
    --slate-light: #5b5b5e;
    --slate-dark: #29292b;
    --paper-white: #ffffff;
    --card-shadow: rgba(0, 0, 0, 0.28);
  }
  * { box-sizing: border-box; margin: 0; padding: 0; }
  html, body {
    width: 1200px;
    height: 914px;
    overflow: hidden;
  }
  body {
    background: var(--stage);
    font-family: "Open Sans", Arial, sans-serif;
    position: relative;
  }
  .card {
    position: absolute;
    left: 250px;
    width: 700px;
    height: 400px;
    border-radius: 4px;
    overflow: hidden;
    box-shadow: 0 10px 26px var(--card-shadow);
  }
  .card--front { top: 40px; background: var(--brand-red); }
  .card--back {
    top: 474px;
    background: linear-gradient(180deg, var(--slate-light) 0%, var(--slate-dark) 100%);
  }
  .card__art {
    position: absolute;
    inset: 0;
    width: 100%;
    height: 100%;
  }
  .holder-name {
    position: absolute;
    top: 22px;
    left: 30px;
    color: var(--paper-white);
    font-size: 17px;
    font-weight: 700;
  }
  .brand-name {
    position: absolute;
    color: var(--paper-white);
    font-weight: 700;
    letter-spacing: -1px;
    line-height: 1;
  }
  .card--front .brand-name {
    top: 110px;
    left: 230px;
    font-size: 92px;
  }
  .card--back .brand-name {
    top: 118px;
    left: 0;
    right: 0;
    text-align: center;
    font-size: 118px;
  }
  .brand-tagline {
    position: absolute;
    top: 262px;
    right: 130px;
    color: var(--brand-red);
    font-size: 23px;
    font-weight: 600;
    letter-spacing: 1px;
  }
  .contact {
    position: absolute;
    display: flex;
    align-items: center;
    gap: 9px;
    color: var(--paper-white);
    font-size: 17px;
    font-weight: 700;
    white-space: nowrap;
  }
  .contact svg { flex: none; width: 18px; height: 18px; }
  .contact--address { left: 28px; top: 290px; }
  .contact--web { left: 28px; top: 330px; }
  .contact--phone { right: 30px; top: 270px; }
</style>
</head>
<body>

<section class="card card--front" aria-label="Business card front">
  <svg class="card__art" viewBox="0 0 700 400" aria-hidden="true">
    <path d="M0 150 C 240 130, 420 250, 520 400 L0 400 Z" fill="var(--ink-black)"/>
    <path d="M0 150 C 240 130, 420 250, 520 400" fill="none" stroke="var(--brand-red)" stroke-width="3" transform="translate(0 14)"/>
  </svg>

  <p class="holder-name">Your Name</p>
  <p class="brand-name">PipTrek</p>

  <p class="contact contact--phone">
    <svg viewBox="0 0 20 20" aria-hidden="true">
      <circle cx="10" cy="10" r="9" fill="none" stroke="var(--paper-white)" stroke-width="2"/>
      <path d="M7 5.5 L8.8 5.5 L9.4 8 L8.3 8.9 C9 10.5 9.8 11.3 11.1 11.8 L12 10.7 L14.5 11.3 L14.5 13 C10 13.5 6.5 10 7 5.5 Z" fill="var(--paper-white)"/>
    </svg>
    970-528-3094
  </p>

  <p class="contact contact--address">
    <svg viewBox="0 0 20 20" aria-hidden="true">
      <path d="M10 1.5 C6.4 1.5 4 4.2 4 7.4 C4 11.6 10 18.5 10 18.5 C10 18.5 16 11.6 16 7.4 C16 4.2 13.6 1.5 10 1.5 Z" fill="var(--brand-red)"/>
      <circle cx="10" cy="7.4" r="2.3" fill="var(--ink-black)"/>
    </svg>
    418 W. Birch Ln., Suite F7 Larkmoor, MT 59031
  </p>

  <p class="contact contact--web">
    <svg viewBox="0 0 20 20" aria-hidden="true">
      <circle cx="10" cy="10" r="8.5" fill="var(--brand-red)"/>
      <g fill="none" stroke="var(--ink-black)" stroke-width="1.2">
        <ellipse cx="10" cy="10" rx="3.6" ry="8.5"/>
        <line x1="1.5" y1="10" x2="18.5" y2="10"/>
        <line x1="3" y1="6" x2="17" y2="6"/>
        <line x1="3" y1="14" x2="17" y2="14"/>
      </g>
    </svg>
    www.TotTrailhub.com
  </p>
</section>

<section class="card card--back" aria-label="Business card back">
  <p class="brand-name">PipTrek</p>
  <p class="brand-tagline">LARKMOOR, MONTANA</p>
</section>

</body>
</html>
```